Letterhead and Envelopes design using existing logo. Logo can be found at ridgemontch.com

Use existing logo (attached) and incorporate in letterhead and envelope designs.

Current logo can be viewed at ridgemontch.com the web site reflect various parent and sub companies. Please see attached as well.

Target Market(s)

Other oil and gas operators.

Industry/Entity Type

Oil And Gas

Font styles to use
Sans Serif

Colors

Designer to choose colors to be used in the design.

Requirements
Must have
• Current logo and address
Nice to have
• Modern, contemporary approach yet incorporate existing traditional design.
• After design is selected for Ridgemont Caldera Holdings I will use similar design for Royalties, Exploration, Energy and Farms with different color schemes.

```html
<!DOCTYPE html>
<html lang="en">
<head>
<meta charset="utf-8">
<title>Ridgemont Caldera Holdings Stationery</title>
<link href="https://fonts.googleapis.com/css2?family=Open+Sans:wght@400;600&display=swap" rel="stylesheet">
<style>
  :root {
    --backdrop: #eeefee;
    --paper: #ffffff;
    --brand-green: #6f9a40;
    --brand-black: #060808;
    --ink: #5f6060;
    --ink-dark: #3d3f3f;
  }
  * { margin: 0; padding: 0; box-sizing: border-box; }
  html, body { width: 1200px; height: 1200px; overflow: hidden; }
  body {
    background: var(--backdrop);
    font-family: "Open Sans", sans-serif;
    color: var(--ink);
    position: relative;
  }
  .sheet {
    position: absolute;
    background: var(--paper);
    overflow: hidden;
    box-shadow: 0 14px 10px -8px rgba(0,0,0,0.35);
  }
  .letterhead { left: 138px; top: 219px; width: 498px; height: 711px; }
  .envelope-back { left: 668px; top: 365px; width: 386px; height: 201px; }
  .envelope-front { left: 668px; top: 603px; width: 386px; height: 201px; }

  .brand-mark {
    position: absolute;
    display: flex;
    align-items: center;
    gap: 7px;
  }
  .brand-mark .dot {
    flex: none;
    border-radius: 50%;
    background: var(--brand-green);
  }
  .brand-mark .name {
    color: var(--ink-dark);
    font-weight: 600;
    line-height: 1.2;
  }
  .letterhead .brand-mark { left: 52px; top: 46px; width: 150px; }
  .letterhead .brand-mark .dot { width: 24px; height: 24px; }
  .letterhead .brand-mark .name { font-size: 12px; }

  .sender-address {
    position: absolute;
    right: 58px; top: 58px;
    text-align: right;
    font-style: normal;
    font-size: 10px;
    line-height: 11.5px;
    letter-spacing: 0.6px;
  }
  .letter-body {
    position: absolute;
    left: 53px; top: 182px;
    width: 392px;
    font-size: 11.2px;
    line-height: 13.3px;
    letter-spacing: -0.2px;
  }
  .salutation { font-weight: 600; font-size: 12.5px; margin-bottom: 1px; letter-spacing: 0; }
  .letter-body p + p { margin-top: 18px; }
  .signature {
    position: absolute;
    left: 345px; top: 513px;
    width: 80px;
    text-align: center;
    font-size: 12.5px;
    color: var(--ink-dark);
  }
  .signature::after {
    content: "";
    display: block;
    margin-top: 14px;
    border-top: 1px solid var(--ink-dark);
  }
  .contact-lines {
    position: absolute;
    left: 53px; top: 629px;
    font-size: 10.5px;
    line-height: 15.2px;
  }
  .corner-block {
    position: absolute;
    right: 0; bottom: 0;
    background: var(--brand-green);
  }
  .corner-block::after {
    content: "";
    position: absolute;
    right: 0; bottom: 0;
    width: 45%; height: 42%;
    background: var(--brand-black);
  }
  .letterhead .corner-block { width: 102px; height: 131px; }
  .envelope-front .corner-block { width: 149px; height: 201px; }

  .flap { position: absolute; left: 0; top: 0; }

  .envelope-front .brand-mark { left: 24px; top: 96px; width: 160px; }
  .envelope-front .brand-mark .dot { width: 14px; height: 14px; }
  .envelope-front .brand-mark .name { font-size: 8px; }
  .envelope-front .return-address {
    position: absolute;
    left: 25px; top: 145px;
    font-size: 7.5px;
    line-height: 10px;
    color: var(--ink-dark);
  }
</style>
</head>
<body>
  <section class="sheet letterhead">
    <div class="brand-mark">
      <span class="dot"></span>
      <span class="name">Ridgemont Caldera Holdings</span>
    </div>
    <address class="sender-address">418 Halvorsen,<br>Dakota Ridge<br>58504</address>
    <div class="letter-body">
      <div class="salutation">Dear Mr.--------</div>
      <p>Lorem Ipsum is simply dummy text of the printing and typesetting industry. Lorem Ipsum has been the industry's standard dummy text ever since the 1500s, when an unknown printer took a galley of type and scrambled it to make a type specimen book. It has survived not only five centuries, but also the leap into electronic typesetting, remaining essentially unchanged. It was popularised in the 1960s with the release of Letraset sheets containing Lorem Ipsum passages, and more recently with desktop publishing software like Aldus PageMaker including versions of Lorem Ipsum.</p>
      <p>Lorem Ipsum is simply dummy text of the printing and typesetting industry. Lorem Ipsum has been the industry's standard dummy text ever since the 1500s, when an unknown printer took a galley of type and scrambled it to make a type specimen book. It has survived not only five centuries, but also the leap into electronic typesetting, remaining essentially unchanged. It was popularised in the 1960s with the release of Letraset sheets containing Lorem Ipsum passages, and more recently with desktop publishing software like Aldus PageMaker including versions of Lorem Ipsum.</p>
    </div>
    <div class="signature">Signature</div>
    <div class="contact-lines">(555) 310.4477<br>reception@ridgemontch.com<br>www.ridgemontch.com</div>
    <div class="corner-block"></div>
  </section>

  <section class="sheet envelope-back">
    <svg class="flap" width="386" height="48" viewBox="0 0 386 48">
      <path d="M0 0 H386 L355 40 Q349 48 337 48 H49 Q37 48 31 40 Z" fill="var(--brand-green)"/>
    </svg>
  </section>

  <section class="sheet envelope-front">
    <div class="brand-mark">
      <span class="dot"></span>
      <span class="name">Ridgemont Caldera Holdings</span>
    </div>
    <div class="return-address">418 Halvorsen, Dakota Ridge 58504<br>(555) 310.4477<br>reception@ridgemontch.com<br>www.ridgemontch.com</div>
    <div class="corner-block"></div>
  </section>
</body>
</html>
```